WWW.VELTRONA.IT BUSINNES CARD

WE NEED A BUSINESS CARD . I HAVE A COMPANY IN ITALY NR 1 IN HAIR MEDICAL CARE AN HAIR REPLECEMENT . IN CARD I NEED WRITE WEB ADDRESS, MAIL , ADDRESS, TELEPHONE NUMBER , AND NAME
IN THE BACK SIDE I NEED MY DOCTOR LOGO .
MY WEB SITE IS WWW.VELTRONA.IT
Updates

Target Market(s)

CONSUMER B2C

Industry/Entity Type

Hair And Beauty

Contact Information for Business Card

I WANT A MEDICAL BUSINESS CARD.

Font styles to use
Other font styles liked:
• VERDANA

Colors
33a6d7
3176b5
85abd2
aedbee
eaf1f7
ffffff

Requirements
Must have
• I NEED MY LOGO AND LOGO OF DR VELTRONA

```html
<!DOCTYPE html>
<html lang="it">
<head>
<meta charset="utf-8">
<title>Veltrona – biglietto da visita</title>
<link rel="stylesheet" href="https://fonts.googleapis.com/css2?family=Varela+Round&display=swap">
<style>
  :root {
    --navy: #0a5296;
    --sky: #29b1e5;
    --sky-soft: #aedbee;
    --paper: #f3f4f5;
    --white: #ffffff;
    --stage: #e6e9ed;
    --hair-dark: #6b3519;
    --hair-light: #9c5a2c;
  }
  * { box-sizing: border-box; margin: 0; padding: 0; }
  html, body { width: 1200px; height: 886px; overflow: hidden; }
  body {
    background: var(--stage);
    font-family: "Varela Round", Verdana, sans-serif;
    position: relative;
  }
  .card {
    position: absolute;
    top: 163px;
    width: 320px;
    height: 560px;
    border-radius: 18px;
    overflow: hidden;
  }
  .card-front { left: 252px; background: var(--paper); }
  .card-back { left: 628px; background: var(--navy); }
  .card-bg { position: absolute; inset: 0; }

  /* front */
  .brand {
    position: absolute; top: 66px; left: 0; width: 100%;
    display: flex; justify-content: center; align-items: center; gap: 10px;
  }
  .brand-dot { width: 30px; height: 30px; border-radius: 50%; background: var(--navy); }
  .brand-name { font-size: 40px; color: var(--navy); line-height: 1; }
  .tagline {
    position: absolute; top: 117px; width: 100%; text-align: center;
    font-size: 10.5px; color: var(--navy); letter-spacing: 0.2px;
  }
  .person-name {
    position: absolute; top: 318px; width: 100%; text-align: center;
    font-size: 27px; font-weight: 400; color: var(--sky); letter-spacing: 0.5px;
  }
  .contact-line {
    position: absolute; top: 382px; width: 100%;
    display: flex; justify-content: center; align-items: center; gap: 8px;
    color: var(--white); font-size: 13.5px;
  }
  .contact-line svg { width: 12px; height: 12px; }
  .contact-item { display: flex; align-items: center; gap: 5px; }
  .website {
    position: absolute; top: 406px; width: 100%;
    display: flex; justify-content: center; align-items: center; gap: 6px;
    color: var(--white); font-size: 12.5px; letter-spacing: 3px;
  }
  .website .rule { width: 42px; height: 1px; background: var(--white); }
  .addresses {
    position: absolute; top: 436px; left: 40px; right: 30px;
    display: grid; grid-template-columns: 1fr 1fr; row-gap: 15px; column-gap: 10px;
    color: var(--white); font-size: 12.5px; line-height: 17px; text-align: center;
  }

  /* back */
  .services {
    position: absolute; top: 44px; left: 24px; list-style: none;
    color: var(--white); font-size: 15px; line-height: 24.3px;
  }
  .services li { position: relative; padding-left: 14px; }
  .services li::before {
    content: ""; position: absolute; left: 0; top: 10px;
    width: 5px; height: 5px; border-radius: 50%; background: var(--sky-soft);
  }
  .mascot {
    position: absolute; left: 196px; top: 14px; width: 112px; height: 532px;
    border-radius: 56px 56px 24px 24px;
    background: linear-gradient(180deg, var(--hair-dark) 0%, var(--hair-light) 100%);
  }
  .back-brand {
    position: absolute; left: 22px; top: 466px;
    font-size: 36px; color: var(--white); line-height: 1;
  }
</style>
</head>
<body>

  <section class="card card-front" aria-label="Fronte del biglietto">
    <svg class="card-bg" viewBox="0 0 320 560" aria-hidden="true">
      <path d="M34 148 Q150 170 280 134" fill="none" stroke="var(--sky)" stroke-width="2.5"/>
      <path d="M0 390 C40 260 140 240 230 220 C290 205 318 180 320 140 L320 560 L0 560 Z" fill="var(--sky)"/>
      <path d="M0 410 C40 290 140 262 232 240 C292 224 320 200 320 160 L320 560 L0 560 Z" fill="var(--navy)"/>
    </svg>
    <div class="brand">
      <span class="brand-dot"></span>
      <span class="brand-name">Veltrona</span>
    </div>
    <p class="tagline">CURA E REINTEGRAZIONE DEI CAPELLI</p>
    <h1 class="person-name">Dario Fennelli</h1>
    <div class="contact-line">
      <span class="contact-item">
        <svg viewBox="0 0 24 24" aria-hidden="true"><path fill="#fff" d="M6.6 10.8a15 15 0 0 0 6.6 6.6l2.2-2.2a1 1 0 0 1 1-.25 11.4 11.4 0 0 0 3.6.57 1 1 0 0 1 1 1V20a1 1 0 0 1-1 1A17 17 0 0 1 3 4a1 1 0 0 1 1-1h3.5a1 1 0 0 1 1 1c0 1.25.2 2.45.57 3.57a1 1 0 0 1-.25 1z"/></svg>
        800527391
      </span>
      <span class="contact-item">
        <svg viewBox="0 0 24 24" aria-hidden="true"><path fill="#fff" d="M2 5h20v14H2z"/><path fill="none" stroke="var(--navy)" stroke-width="2" d="M2 5l10 8 10-8"/></svg>
        Dario@veltrona.it
      </span>
    </div>
    <div class="website"><span class="rule"></span>www.veltrona.it<span class="rule"></span></div>
    <div class="addresses">
      <p>Via dei Tigli 112<br>57126 Livorno, Italy</p>
      <p>Via Sarzana 36<br>31100 Treviso, Italy</p>
      <p>Via dei Tigli 112<br>57126 Livorno, Italy</p>
      <p>Via Orti 19<br>37122 Verona, Italy</p>
    </div>
  </section>

  <section class="card card-back" aria-label="Retro del biglietto">
    <svg class="card-bg" viewBox="0 0 320 560" aria-hidden="true">
      <path d="M250 0 C200 60 200 200 210 320 C220 440 200 520 190 560 L320 560 L320 0 Z" fill="var(--sky)"/>
    </svg>
    <ul class="services">
      <li>Consulenza</li>
      <li>Check-up</li>
      <li>hairtest</li>
      <li>trattamenti e<br>prodotti tricologici</li>
      <li>stimolazione delle<br>cellule staminali</li>
      <li>autotrapianto fue</li>
      <li>fotostimolazione</li>
      <li>ossigenoterapia</li>
      <li>parrucche medicali</li>
      <li>soluzione invisibili</li>
      <li>infoltimento naturale</li>
    </ul>
    <div class="mascot" role="img" aria-label="Illustrazione della mascotte: un capello castano con camice da medico"></div>
    <p class="back-brand">Veltrona</p>
  </section>

</body>
</html>
```